Verdant Holdings SA Business Cards

Dear all,
Thank you for reading my brief and project. My company is doing doing advisory in real estate and to comapnies + real estates services as asset management, brokerage, development etc.
I would like to get a business card for my company which is clear, professionnal and serious.
Please have a look to the attachement to see the logos of the company

Industry/Entity Type

Real Estate

Contact Information for Business Card

I would like to have in the business card the following
Principal side:
- Logo of the company (or Monogram)
- First and Last Name (Marcel Tobler)
- Mobile number
- email address

Second side:
- Address (Chemin des Vergers 17, 1292 Chambésy - Switzerland)
- website (www.verdantholdings.ch)

Requirements
Must have
• Refer to the typeface and logo colors

```html
<!DOCTYPE html>
<html lang="en">
<head>
<meta charset="utf-8">
<title>Verdant Holdings SA — Business Cards</title>
<link href="https://fonts.googleapis.com/css2?family=Questrial&display=swap" rel="stylesheet">
<style>
  :root {
    --backdrop: #253549;
    --navy: #2b3a4f;
    --blue: #1473c8;
    --paper: #ffffff;
    --ink-light: #e8edf3;
  }
  * { margin: 0; padding: 0; box-sizing: border-box; }
  html, body { width: 1200px; height: 1200px; overflow: hidden; }
  body {
    background: var(--backdrop);
    font-family: "Questrial", "Century Gothic", sans-serif;
    position: relative;
  }
  .card {
    position: absolute;
    left: 160px;
    width: 880px;
    height: 527px;
    background: var(--paper);
    overflow: hidden;
    box-shadow: 0 14px 28px rgba(0,0,0,0.35);
  }
  .card--front { top: 53px; }
  .card--back { top: 620px; }

  .brand {
    position: absolute;
    display: flex;
    align-items: center;
    gap: 16px;
    color: var(--navy);
    text-transform: uppercase;
    letter-spacing: 0.04em;
    white-space: nowrap;
  }
  .brand__mark {
    width: 20px; height: 20px;
    border-radius: 50%;
    background: var(--blue);
    flex: none;
  }
  .card--front .brand { left: 56px; top: 246px; font-size: 22px; }
  .card--back .brand { left: 0; right: 0; justify-content: center; top: 182px; font-size: 30px; }

  .front__panel {
    position: absolute;
    left: 411px; top: 0;
    width: 469px; height: 100%;
    background: var(--navy);
  }
  .front__tab { position: absolute; left: 399px; top: 258px; }
  .front__name {
    position: absolute;
    left: 456px; top: 68px;
    color: var(--paper);
    font-size: 37px;
  }
  .contact {
    position: absolute;
    left: 458px;
    color: var(--ink-light);
    font-size: 23px;
  }
  .contact--phone { top: 312px; }
  .contact--email { top: 378px; }

  .back__band {
    position: absolute;
    left: 0; top: 416px;
    width: 100%; height: 111px;
    background: var(--navy);
  }
  .back__ribbon { position: absolute; left: 0; top: 394px; }
  .back__web {
    position: absolute;
    left: 175px; width: 528px;
    top: 400px;
    text-align: center;
    color: var(--paper);
    font-size: 18px;
    letter-spacing: 0.28em;
  }
  .back__address {
    position: absolute;
    left: 0; right: 0; top: 470px;
    display: flex;
    justify-content: center;
    align-items: center;
    gap: 16px;
    color: var(--ink-light);
    font-size: 23px;
  }
</style>
</head>
<body>

<section class="card card--front" aria-label="Business card front">
  <div class="brand"><span class="brand__mark"></span>Verdant Holdings SA</div>
  <div class="front__panel"></div>
  <svg class="front__tab" width="34" height="210" viewBox="0 0 34 210">
    <polygon points="0,0 30,14 30,196 0,210" fill="var(--blue)"/>
    <!-- phone -->
    <path d="M9 64c0 9 6 16 14 17l3-4-4-3-2 2c-3-1-6-4-7-7l2-2-3-4z" fill="var(--paper)"/>
    <!-- envelope -->
    <rect x="7" y="128" width="18" height="13" fill="var(--paper)"/>
    <polyline points="7,128 16,136 25,128" fill="none" stroke="var(--blue)" stroke-width="1.6"/>
  </svg>
  <div class="front__name">Marcel Tobler</div>
  <div class="contact contact--phone">+41 22 555 0178</div>
  <div class="contact contact--email">contact@verdantholdings.ch</div>
</section>

<section class="card card--back" aria-label="Business card back">
  <div class="brand"><span class="brand__mark"></span>Verdant Holdings SA</div>
  <div class="back__band"></div>
  <svg class="back__ribbon" width="880" height="44" viewBox="0 0 880 44">
    <polygon points="175,0 703,0 673,43 205,43" fill="var(--blue)"/>
  </svg>
  <div class="back__web">www.verdantholdings.ch</div>
  <div class="back__address">
    <svg width="24" height="26" viewBox="0 0 24 26" aria-hidden="true">
      <path d="M12 1a7 7 0 0 0-7 7c0 5 7 12 7 12s7-7 7-12a7 7 0 0 0-7-7z" fill="var(--paper)"/>
      <circle cx="12" cy="8" r="2.6" fill="var(--navy)"/>
      <rect x="2" y="22" width="20" height="3" fill="var(--paper)"/>
    </svg>
    <span>Chemin des Vergers 17, 1292 Chambésy - Switzerland</span>
  </div>
</section>

</body>
</html>
```